We need a letterhead design for a new international company based in Luanda, Angola called "Halvorn Corporation". Halvorn Corporation is a multiservice private company. We provides services for the following sectors: Oil & Gas industry, Government, and the Public.

Target Market(s)

Board of directors of the following sectors: Oil & Gas industry, Government, and the Public.

Industry/Entity Type

Government

Requirements
Must have
• Halvorn Corporation logo

```html
<!DOCTYPE html>
<html lang="en">
<head>
<meta charset="utf-8">
<title>Halvorn Corporation Letterhead</title>
<link href="https://fonts.googleapis.com/css2?family=Questrial&display=swap" rel="stylesheet">
<style>
  :root {
    --backdrop: #d9d9d9;
    --paper: #f4f4f4;
    --ink: #2b2b2b;
    --ink-soft: #5a5a5a;
    --gold: #b5970f;
    --band: #2a2a2a;
  }
  * { margin: 0; padding: 0; box-sizing: border-box; }
  html, body {
    width: 1200px;
    height: 968px;
    overflow: hidden;
    background: var(--backdrop);
    font-family: "Questrial", sans-serif;
  }
  .letterhead {
    position: absolute;
    left: 282px;
    top: 34px;
    width: 636px;
    height: 900px;
    background: var(--paper);
    box-shadow: 0 6px 24px rgba(0,0,0,0.12);
    overflow: hidden;
  }
  .brand {
    position: absolute;
    left: 44px;
    top: 46px;
    display: flex;
    align-items: center;
    gap: 10px;
  }
  .brand-dot {
    width: 26px;
    height: 26px;
    border-radius: 50%;
    background: var(--gold);
  }
  .brand-name {
    font-size: 24px;
    color: var(--ink);
    letter-spacing: 0.5px;
  }
  .contact {
    position: absolute;
    right: 40px;
    top: 106px;
    display: flex;
    gap: 18px;
    font-size: 9px;
    line-height: 1.6;
    color: var(--ink-soft);
  }
  .contact-line {
    display: flex;
    align-items: center;
    gap: 5px;
  }
  .contact-icon {
    width: 9px;
    height: 9px;
    border-radius: 50%;
    background: var(--gold);
    flex: none;
  }
  .footer-wave {
    position: absolute;
    left: 0;
    bottom: 0;
    width: 636px;
    height: 220px;
  }
</style>
</head>
<body>
  <main class="letterhead">
    <header class="brand">
      <span class="brand-dot"></span>
      <span class="brand-name">Halvorn Corporation</span>
    </header>

    <address class="contact" style="font-style:normal">
      <div class="contact-address">
        <div>Rua do Farol</div>
        <div>Luanda, Angola</div>
      </div>
      <div class="contact-phones">
        <div class="contact-line"><span class="contact-icon"></span>+244 222 000 410</div>
        <div class="contact-line"><span class="contact-icon"></span>+244 222 000 411</div>
      </div>
      <div class="contact-web">
        <div class="contact-line"><span class="contact-icon"></span>info@halvorn-corp.com</div>
        <div class="contact-line"><span class="contact-icon"></span>www.halvorn-corp.com</div>
      </div>
    </address>

    <svg class="footer-wave" viewBox="0 0 636 220" preserveAspectRatio="none" aria-hidden="true">
      <path d="M0 40 C 150 40, 280 150, 420 185 C 520 208, 600 205, 636 200 L 636 220 L 0 220 Z" fill="var(--band)"/>
      <path d="M0 30 C 170 20, 290 130, 430 168 C 520 192, 590 196, 636 190 L 636 194 C 590 200, 520 198, 430 176 C 290 140, 170 30, 0 36 Z" fill="var(--gold)"/>
    </svg>
  </main>
</body>
</html>
```